Semi-anonymous photo sharing and messaging app

Design app interface. App is needed for semi-anonymous communication.

For instance if you are on a tour bus, and you just met some people there. You want to send them pictures, but you don't want to give your chatterly / email / phone number. So instead you use this app - current name is "eLumvo" but you can also suggest a name if it fits really well with the theme of the design.

The initial version of the app is in the tivora store
https://shop.tivora-apps.example/item?id=net.k7mzpwq2rt84vbnhsy3lc

the web version of this app is located here
https://plumtidelanternharbor.example/

it is called Plum Tide Lantern Harbor, because the password is four common words, and if you know those words, you can open the chat room.

As you can see app looks very poorly, and needs to be designed from bottom up. App should look nothing like it looks now. it should have original and easily recognizable feel to it.

I'm attaching screen-shots of the current app. Two screens - you enter password on one screen (or choose one of the existing "rooms") - you chat with peers on the second screen

It should be something neutral, so it's mainly for travellers, but could be used by anyone else. It should have vibe of comfort and security, but at the same time adventure and fun.

Please come back with more questions!

Target Market(s)

Travellers, mostly
single, groups,

Industry/Entity Type

Communication

Font styles to use
Sans Serif

Requirements
Must have
• original, light feel
• recognizable
• unique

```html
<!DOCTYPE html>
<html lang="en">
<head>
<meta charset="utf-8">
<title>Plum Tide Lantern Harbor – App Screens</title>
<link href="https://fonts.googleapis.com/css2?family=Marcellus&family=Arimo:wght@400;700&display=swap" rel="stylesheet">
<style>
  :root {
    --page-bg: #e6e6e6;
    --bar-black: #050505;
    --header-white: #f1f1f1;
    --accent-orange: #f39200;
    --accent-orange-soft: rgba(240, 150, 20, 0.85);
    --navy: #1f3f6e;
    --navy-border: #5b7aa6;
    --deep-blue: #0e2a4a;
    --teal: #2b8fa8;
    --field-bg: rgba(8, 30, 40, 0.72);
    --field-border: rgba(170, 200, 210, 0.55);
    --text-white: #ffffff;
    --text-muted: #9fb3bd;
    --brand-text: #1e2a36;
    --brand-dot: #e2621b;
  }
  * { box-sizing: border-box; margin: 0; padding: 0; }
  html, body { width: 1200px; height: 900px; overflow: hidden; }
  body {
    background: var(--page-bg);
    font-family: "Arimo", Arial, sans-serif;
    position: relative;
  }
  .screen {
    position: absolute;
    top: 112px;
    width: 380px;
    height: 672px;
    overflow: hidden;
    background: var(--deep-blue);
  }
  .screen--login { left: 140px; }
  .screen--room { left: 642px; }

  .screen__backdrop {
    position: absolute;
    inset: 90px 0 0 0;
    background:
      radial-gradient(ellipse 60% 35% at 75% 80%, rgba(190, 215, 225, 0.55), transparent 70%),
      radial-gradient(ellipse 70% 40% at 60% 25%, rgba(60, 170, 190, 0.55), transparent 70%),
      linear-gradient(160deg, #163c66 0%, #1d6f8c 45%, #0f3150 75%, #0b2340 100%);
  }

  .status-bar {
    position: absolute; top: 0; left: 0; right: 0; height: 24px;
    background: var(--bar-black);
    color: var(--text-white);
    font-size: 12px;
    display: flex; align-items: center; justify-content: space-between;
    padding: 0 10px;
  }
  .status-bar__signal { letter-spacing: 1px; font-size: 10px; }
  .status-bar__time { position: absolute; left: 0; right: 0; text-align: center; }
  .status-bar__battery { display: flex; align-items: center; gap: 4px; }
  .battery-icon { width: 22px; height: 10px; border: 1px solid #fff; border-radius: 2px; position: relative; }
  .battery-icon::before { content: ""; position: absolute; left: 1px; top: 1px; bottom: 1px; width: 6px; background: #fff; }

  .app-header {
    position: absolute; top: 24px; left: 0; right: 0; height: 66px;
    background: var(--header-white);
    border-bottom: 2px solid var(--accent-orange);
    display: flex; flex-direction: column; align-items: center; justify-content: center; gap: 5px;
  }
  .brand-mark { width: 30px; height: 30px; border-radius: 50%; background: var(--brand-dot); }
  .brand-name { font-size: 10px; color: var(--brand-text); }

  .heading {
    position: absolute; left: 0; right: 0;
    font-family: "Marcellus", Georgia, serif;
    color: var(--text-white);
    text-align: center;
    font-weight: 700;
    -webkit-text-stroke: 0.6px var(--text-white);
  }
  .heading--login { top: 116px; font-size: 30px; }
  .heading--room { top: 148px; font-size: 21px; }
  .rule { position: absolute; height: 1px; background: rgba(200, 220, 230, 0.45); }

  .word-rail { position: absolute; left: 46px; top: 173px; width: 3px; height: 235px; background: rgba(210, 225, 235, 0.55); }
  .word-row { position: absolute; left: 18px; width: 350px; height: 34px; }
  .word-row__badge {
    position: absolute; left: 0; top: 7px; width: 58px; height: 20px;
    background: var(--accent-orange); color: var(--text-white);
    font-family: "Marcellus", Georgia, serif; font-size: 12px; font-weight: 700;
    display: flex; align-items: center; justify-content: center; border-radius: 2px;
  }
  .field {
    position: absolute; background: var(--field-bg);
    border: 1px solid var(--field-border); border-radius: 4px;
    color: var(--text-muted); font-size: 12px; display: flex; align-items: center; padding-left: 8px;
  }
  .word-row__field { left: 72px; top: 0; width: 277px; height: 34px; }

  .btn {
    position: absolute; display: flex; align-items: center; justify-content: center;
    color: var(--text-white); font-family: "Marcellus", Georgia, serif; font-weight: 700;
  }
  .btn--small {
    height: 23px; font-size: 10px; background: var(--navy);
    border: 1px solid var(--navy-border); border-radius: 3px;
  }
  .btn--wide { left: 64px; width: 252px; height: 23px; font-size: 14px; border-radius: 2px; }
  .btn--send { top: 288px; background: var(--accent-orange); }
  .btn--exit { top: 321px; background: var(--navy); border: 1px solid var(--navy-border); }
  .btn--photo {
    left: 215px; top: 610px; width: 150px; height: 37px; border-radius: 19px;
    background: var(--accent-orange); border: 1px solid #ffc35a;
    font-family: "Arimo", Arial, sans-serif; font-weight: 400; font-size: 14px; gap: 8px;
  }

  .recent-title {
    position: absolute; left: 20px; top: 490px;
    font-family: "Marcellus", Georgia, serif; font-size: 21px; font-weight: 700;
    color: var(--text-white); -webkit-text-stroke: 0.5px var(--text-white);
  }
  .recent-box {
    position: absolute; left: 20px; top: 523px; width: 349px; height: 47px;
    background: var(--accent-orange-soft); border: 1px solid #f6b24a; border-radius: 2px;
  }

  .message-count {
    position: absolute; left: 66px; width: 245px; top: 199px;
    display: flex; justify-content: space-between; color: var(--text-white); font-size: 12px;
  }
  .message-field { left: 17px; top: 229px; width: 345px; height: 41px; border-radius: 5px; }

  .bottom-stripe { position: absolute; left: 0; right: 0; bottom: 0; height: 5px; background: var(--accent-orange); }
</style>
</head>
<body>

  <section class="screen screen--login" aria-label="Enter words screen">
    <div class="screen__backdrop" role="img" aria-label="Blue-teal background photo of hands holding a phone"></div>
    <div class="status-bar">
      <span class="status-bar__signal">●●●○○</span>
      <span class="status-bar__time">11:19 PM</span>
      <span class="status-bar__battery">31% <span class="battery-icon"></span></span>
    </div>
    <header class="app-header">
      <span class="brand-mark"></span>
      <span class="brand-name">Plum Tide Lantern Harbor</span>
    </header>

    <h1 class="heading heading--login">Enter Four Words!</h1>
    <div class="rule" style="left:18px; width:346px; top:156px;"></div>

    <div class="word-rail"></div>
    <div class="word-row" style="top:190px;"><span class="word-row__badge">Word:</span><span class="field word-row__field">ORDER:</span></div>
    <div class="word-row" style="top:246px;"><span class="word-row__badge">Word:</span><span class="field word-row__field">ORDER:</span></div>
    <div class="word-row" style="top:301px;"><span class="word-row__badge">Word:</span><span class="field word-row__field">ORDER:</span></div>
    <div class="word-row" style="top:357px;"><span class="word-row__badge">Word:</span><span class="field word-row__field">ORDER:</span></div>

    <span class="btn btn--small" style="left:212px; top:403px; width:101px;">RANDOM WORDS</span>
    <span class="btn btn--small" style="left:317px; top:403px; width:50px;">ENTER</span>

    <h2 class="recent-title">Recent</h2>
    <div class="rule" style="left:105px; width:260px; top:504px;"></div>
    <div class="recent-box"></div>

    <div class="bottom-stripe"></div>
  </section>

  <section class="screen screen--room" aria-label="Chat room screen">
    <div class="screen__backdrop" role="img" aria-label="Blue-teal background photo of hands holding a phone"></div>
    <div class="status-bar">
      <span class="status-bar__signal">●●●○○</span>
      <span class="status-bar__time">11:19 PM</span>
      <span class="status-bar__battery">31% <span class="battery-icon"></span></span>
    </div>
    <header class="app-header">
      <span class="brand-mark"></span>
      <span class="brand-name">Plum Tide Lantern Harbor</span>
    </header>

    <h1 class="heading heading--room">Anode House Love Relative</h1>
    <div class="rule" style="left:61px; width:254px; top:192px;"></div>
    <div class="message-count"><span>Total messages:</span><span>0</span></div>
    <div class="field message-field"></div>

    <span class="btn btn--wide btn--send">SEND</span>
    <span class="btn btn--wide btn--exit">EXIT</span>

    <span class="btn btn--photo">
      <svg width="26" height="20" viewBox="0 0 26 20" aria-hidden="true">
        <rect x="1" y="4" width="24" height="15" rx="2" fill="none" stroke="#fff" stroke-width="1.6"/>
        <rect x="8" y="1" width="9" height="4" rx="1" fill="none" stroke="#fff" stroke-width="1.4"/>
        <circle cx="13" cy="11.5" r="4.5" fill="none" stroke="#fff" stroke-width="1.6"/>
      </svg>
      Add photo
    </span>

    <div class="bottom-stripe"></div>
  </section>

</body>
</html>
```